Black Matte card with samurai logo which I would like it to be textured and company name on one side and on the other side I would like the company information with the rinzo (Face logo) Sushi logo. Double Sided card.

Target Market(s)

majority customers are University students, University sororities and fraternities.

Industry/Entity Type

It Company

Contact Information for Business Card

Rinzo Sushi
217 W. Larkmoor St
Tucson, AZ 85742
Phone (520)463-1907
Fax (520)381-5046
E-mail: Rinzosushitucson@plimvox.com
FB: Rinzosushitucson
Twitter: Rinzosushitucson

Font styles to use
Other font styles liked:
• Present Normal

```html
<!DOCTYPE html>
<html lang="en">
<head>
<meta charset="utf-8">
<title>Rinzo Sushi business card</title>
<link rel="stylesheet" href="https://fonts.googleapis.com/css2?family=Source+Sans+3:wght@400;600&display=swap">
<style>
  :root {
    --bg: #e9e6e1;
    --paper: #ffffff;
    --ink: #2b2728;
    --red: #b3312b;
    --black: #231f20;
    --slate-light: #3b3b3b;
    --slate-dark: #0f0f0f;
    --art-dark: #2a2526;
    --art-red: #a9322c;
  }
  * { margin: 0; padding: 0; box-sizing: border-box; }
  html, body { width: 1200px; height: 1099px; overflow: hidden; background: var(--bg); }
  body { position: relative; font-family: "Source Sans 3", sans-serif; color: var(--ink); }

  .card {
    position: absolute;
    width: 901px; height: 514px;
    border-radius: 26px;
    overflow: hidden;
    box-shadow: 0 4px 14px rgba(0,0,0,.25);
  }
  .card-front { left: 25px; top: 25px; background: var(--paper); }
  .card-back {
    left: 272px; top: 564px;
    background: linear-gradient(180deg, var(--slate-light), var(--slate-dark) 55%, var(--slate-light));
  }

  .mascot-art {
    position: absolute;
    border-radius: 10px;
    background: radial-gradient(ellipse at 50% 45%, var(--art-dark) 55%, var(--art-red) 100%);
  }
  .card-front .mascot-art { left: 149px; top: 76px; width: 208px; height: 189px; }
  .card-back .mascot-art { left: 299px; top: 51px; width: 307px; height: 284px; }

  .brand-name { position: absolute; color: var(--red); font-weight: 400; white-space: nowrap; }
  .card-front .brand-name { left: 150px; top: 268px; width: 210px; text-align: center; font-size: 58px; line-height: 1; }
  .card-front .brand-sub { position: absolute; left: 150px; top: 330px; width: 210px; text-align: center; font-size: 32px; color: var(--red); line-height: 1; }
  .card-back .brand-name { left: 0; width: 901px; top: 352px; text-align: center; font-size: 76px; line-height: 1; }

  .divider { position: absolute; left: 421px; top: 134px; width: 1px; height: 212px; background: #c9c9c9; }

  .contact-list { position: absolute; left: 455px; top: 144px; list-style: none; font-size: 22px; line-height: 38px; }
  .contact-list li { display: flex; align-items: center; gap: 10px; }
  .contact-list svg { width: 22px; height: 22px; fill: var(--red); }

  .address { position: absolute; left: 451px; top: 276px; font-size: 22px; line-height: 32px; font-style: normal; }

  .swoosh { position: absolute; left: 0; top: 0; width: 901px; height: 514px; }

  .social-list { position: absolute; left: 616px; top: 442px; list-style: none; color: #fff; font-size: 21px; line-height: 38px; }
  .social-list li { display: flex; align-items: center; gap: 10px; }
  .social-list .mark { width: 24px; height: 24px; background: var(--red); }
</style>
</head>
<body>
  <section class="card card-front">
    <svg class="swoosh" viewBox="0 0 901 514" aria-hidden="true">
      <path d="M0 446 Q440 376 901 416" fill="none" stroke="var(--black)" stroke-width="6"/>
      <path d="M0 458 Q330 420 600 432 Q300 444 0 492 Z" fill="var(--red)"/>
      <path d="M0 505 Q430 430 901 424 L901 514 L0 514 Z" fill="var(--black)"/>
    </svg>
    <div class="mascot-art" role="img" aria-label="Samurai mascot illustration holding a sword and a fish"></div>
    <div class="brand-name">rinzo</div>
    <div class="brand-sub">sushi</div>
    <div class="divider"></div>
    <ul class="contact-list">
      <li><svg viewBox="0 0 24 24"><path d="M6.6 10.8a15 15 0 0 0 6.6 6.6l2.2-2.2a1 1 0 0 1 1-.3 11 11 0 0 0 3.6.6 1 1 0 0 1 1 1V20a1 1 0 0 1-1 1A17 17 0 0 1 3 4a1 1 0 0 1 1-1h3.5a1 1 0 0 1 1 1 11 11 0 0 0 .6 3.6 1 1 0 0 1-.3 1z"/></svg>(520) 463-1907</li>
      <li><svg viewBox="0 0 24 24"><path d="M6 3h12v5H6zM3 9h18a1 1 0 0 1 1 1v7h-4v4H6v-4H2v-7a1 1 0 0 1 1-1zm5 6v4h8v-4z"/></svg>(520) 381-5046</li>
      <li><svg viewBox="0 0 24 24"><path d="M2 5h20v14H2zm2 2v.5l8 5 8-5V7z"/></svg>rinzosushitucson@plimvox.com</li>
    </ul>
    <address class="address">217 W. Larkmoor St<br>Tucson, AZ 85742</address>
    <ul class="social-list">
      <li><span class="mark"></span>rinzosushitucson</li>
      <li><span class="mark"></span>rinzosushitucson</li>
    </ul>
  </section>

  <section class="card card-back">
    <div class="mascot-art" role="img" aria-label="Samurai mascot illustration holding a sword and a fish"></div>
    <div class="brand-name">rinzo sushi</div>
  </section>
</body>
</html>
```